Welcome signage for KWT Software Consulting Company

I need Welcome signage for KWT Consulting company Office Window. We are a Computer software company that offers software Implementation and Training for our Customers windows size 1. 900mm high 750mm wide. size 2. 1000mm high 700 wide.
Please review our website for branding and ideas.
The poster needs to contain our logo, website www.kwtadvisory-example.net.au and ph number 1300 46 81 02 , and the strap line... Empowering businesses with software choice.
Updates

Hi I'm really keen to find the perfect design. I had decided on one however the designer was dismissed from the group by admin so here I go again. Please read the briefs already in the information and hopefully I am excited by new submissions when I arrive to work on Monday xxx Thanks heaps fellow Designers x

```html
<!DOCTYPE html>
<html lang="en">
<head>
<meta charset="utf-8">
<title>KWT Consulting – Window Signage</title>
<link rel="stylesheet" href="https://fonts.googleapis.com/css2?family=Open+Sans:wght@300;400;700&display=swap">
<style>
  :root {
    --backdrop-dark: #6e6e6e;
    --backdrop-light: #a4a4a4;
    --paper: #ffffff;
    --band-grey: #cfcfcf;
    --ink-grey: #5b5b5b;
    --orange-deep: #e9680f;
    --orange-light: #f8ba20;
    --text-light: #ffffff;
  }
  * { margin: 0; padding: 0; box-sizing: border-box; }
  html, body { width: 893px; height: 1200px; overflow: hidden; }
  body {
    position: relative;
    background: linear-gradient(135deg, var(--backdrop-dark), var(--backdrop-light));
    font-family: "Open Sans", Arial, sans-serif;
  }
  .sign {
    position: absolute;
    left: 58px;
    background: var(--paper);
    overflow: hidden;
  }
  .sign--small { top: 59px; width: 602px; height: 501px; }
  .sign--large { top: 607px; width: 765px; height: 535px; }
  .sign__shape { position: absolute; inset: 0; width: 100%; height: 100%; }
  .line {
    position: absolute;
    left: 0; right: 0;
    text-align: center;
    color: var(--text-light);
    white-space: nowrap;
    transform: translateY(-50%);
  }
  .brand {
    position: absolute; left: 0; right: 0;
    display: flex; align-items: center; justify-content: center; gap: 14px;
    transform: translateY(-50%);
  }
  .brand__dot { border-radius: 50%; background: var(--orange-deep); flex: none; }
  .brand__name { color: var(--ink-grey); font-weight: 400; letter-spacing: 0.01em; }
  .tagline { font-weight: 300; line-height: 1; }
  .divider {
    position: absolute; left: 50%; height: 1px;
    background: var(--text-light); transform: translateX(-50%);
  }
  .phone { font-weight: 700; letter-spacing: -0.01em; line-height: 1; }
  .web { font-weight: 400; letter-spacing: 0.34em; line-height: 1; }

  .sign--small .brand { top: 100px; }
  .sign--small .brand__dot { width: 52px; height: 52px; }
  .sign--small .brand__name { font-size: 50px; }
  .sign--small .tagline--one { top: 269px; font-size: 40px; }
  .sign--small .tagline--two { top: 321px; font-size: 40px; }
  .sign--small .divider { top: 365px; width: 130px; }
  .sign--small .phone { top: 413px; font-size: 46px; }
  .sign--small .web { top: 460px; font-size: 14px; letter-spacing: 0.3em; }

  .sign--large .brand { top: 98px; }
  .sign--large .brand__dot { width: 58px; height: 58px; }
  .sign--large .brand__name { font-size: 56px; }
  .sign--large .tagline--one { top: 287px; font-size: 49px; }
  .sign--large .tagline--two { top: 349px; font-size: 49px; }
  .sign--large .divider { top: 398px; width: 150px; }
  .sign--large .phone { top: 453px; font-size: 55px; }
  .sign--large .web { top: 506px; font-size: 17px; letter-spacing: 0.3em; }
</style>
</head>
<body>

  <section class="sign sign--small">
    <svg class="sign__shape" viewBox="0 0 602 501" preserveAspectRatio="none" aria-hidden="true">
      <defs>
        <linearGradient id="fill-small" x1="0" x2="1" y1="0" y2="0">
          <stop offset="0" stop-color="var(--orange-deep)"/>
          <stop offset="1" stop-color="var(--orange-light)"/>
        </linearGradient>
      </defs>
      <polygon points="0,127 301,222 602,127 602,155 301,222 0,155" fill="var(--band-grey)"/>
      <polygon points="0,155 301,222 602,155 602,501 0,501" fill="url(#fill-small)"/>
    </svg>
    <div class="brand"><span class="brand__dot"></span><span class="brand__name">KWT Consulting</span></div>
    <p class="line tagline tagline--one">Empowering businesses</p>
    <p class="line tagline tagline--two">with software choice.</p>
    <div class="divider"></div>
    <p class="line phone">1300 46 81 02</p>
    <p class="line web">www.kwtadvisory-example.net.au</p>
  </section>

  <section class="sign sign--large">
    <svg class="sign__shape" viewBox="0 0 765 535" preserveAspectRatio="none" aria-hidden="true">
      <defs>
        <linearGradient id="fill-large" x1="0" x2="1" y1="0" y2="0">
          <stop offset="0" stop-color="var(--orange-deep)"/>
          <stop offset="1" stop-color="var(--orange-light)"/>
        </linearGradient>
      </defs>
      <polygon points="0,110 382,233 765,110 765,144 382,233 0,144" fill="var(--band-grey)"/>
      <polygon points="0,144 382,233 765,144 765,535 0,535" fill="url(#fill-large)"/>
    </svg>
    <div class="brand"><span class="brand__dot"></span><span class="brand__name">KWT Consulting</span></div>
    <p class="line tagline tagline--one">Empowering businesses</p>
    <p class="line tagline tagline--two">with software choice.</p>
    <div class="divider"></div>
    <p class="line phone">1300 46 81 02</p>
    <p class="line web">www.kwtadvisory-example.net.au</p>
  </section>

</body>
</html>
```